One page website for a Personal Injury Law Firm

Design and code a one page website in WordPress for the Brightwell Law Firm, which is a a personal injury law firm located in Coral Gables, Florida. Please note: if you want to change the color pallete for the logo and for the web design , that is fine by me.

Target Market(s)

Those injured in accidents that need legal representation

Industry/Entity Type

Legal

Coding

Coded - Design and coding required

Number of Pages Required

1 page

Font styles to use
Other font styles liked:
• Montserrat

```html
<!DOCTYPE html>
<html lang="en">
<head>
<meta charset="utf-8">
<title>Brightwell Law Firm</title>
<link href="https://fonts.googleapis.com/css2?family=Gelasio:wght@400;500&family=Open+Sans:wght@400;600;700&display=swap" rel="stylesheet">
<style>
:root{
  --navy:#0f1330;
  --gold:#d4a86a;
  --gold-dark:#c59552;
  --ink:#1b1b1f;
  --muted:#6f6f76;
  --cream:#faf7f2;
  --card:#f4f4f4;
  --white:#ffffff;
}
*{box-sizing:border-box;margin:0;padding:0}
html,body{width:1200px;height:4694px;overflow:hidden}
body{position:relative;background:var(--white);font-family:"Open Sans",sans-serif;color:var(--ink)}
.abs{position:absolute}
.serif{font-family:"Gelasio",serif;font-weight:400}
.btn{position:absolute;background:var(--gold);color:var(--white);font-weight:600;font-size:15px;display:flex;align-items:center;justify-content:center}
.ph{position:absolute}

/* header */
.site-header{position:absolute;top:0;left:0;width:1200px;height:78px;background:var(--white)}
.brand{position:absolute;left:70px;top:6px;width:110px;text-align:center;color:var(--navy)}
.brand .mark{width:22px;height:22px;border:2px solid var(--gold);border-radius:50%;margin:0 auto 2px}
.brand .name{font-family:"Gelasio",serif;font-size:22px;line-height:24px}
.brand .sub{font-family:"Gelasio",serif;font-size:7px;letter-spacing:1px}
.main-nav{position:absolute;left:279px;top:28px;display:flex;gap:20px;font-size:14px;color:var(--ink)}
.signin{position:absolute;left:950px;top:28px;font-size:14px}

/* hero */
.hero{position:absolute;top:78px;left:0;width:1200px;height:584px;background:var(--navy)}
.hero h1{position:absolute;left:70px;top:134px;width:500px;font-size:40px;line-height:56px;color:var(--white)}
.hero p{position:absolute;left:70px;top:312px;width:480px;font-size:18px;line-height:28px;color:var(--white)}

/* about */
.about-deco{left:0;top:748px;width:483px;height:467px;background:linear-gradient(135deg,#f1f1f3,#fbfbfc)}
.section-title{font-size:40px;line-height:48px;color:var(--ink)}
.body-copy{font-size:15px;line-height:24.5px;color:#55555c}

/* strategy */
.band{position:absolute;left:0;width:1200px;background:var(--cream)}
.center{text-align:center;width:1200px;left:0}
.strat-card .t{font-size:20px;color:var(--ink);margin-top:24px}
.strat-card .d{font-size:12.5px;line-height:20px;color:var(--muted);margin-top:8px}
.strat-card .l{font-size:13px;color:var(--gold);margin-top:14px}

/* features */
.feature{position:absolute;top:2508px;height:192px;background:var(--card);padding:24px 20px}
.feature.dark{background:var(--navy);color:var(--white)}
.feature .head{display:flex;align-items:center;gap:18px;height:60px}
.feature .head span{font-family:"Gelasio",serif;font-size:16px;line-height:22px}
.feature p{font-size:11.5px;line-height:18px;margin-top:20px;color:var(--muted)}
.feature.dark p{color:var(--white)}

/* practice */
.practice{position:absolute;width:250px}
.practice h3{font-family:"Gelasio",serif;font-weight:400;font-size:23px;margin-top:14px}
.practice p{font-size:14px;line-height:21px;color:var(--muted);margin-top:6px}
.divider{position:absolute;width:1px;background:#d8cfc2}

/* testimonials */
.testi{position:absolute;top:3812px;width:332px;height:351px;background:#f5f5f5;padding:32px 20px}
.testi .q{font-family:"Gelasio",serif;font-size:60px;line-height:40px;color:var(--gold)}
.testi h4{font-family:"Gelasio",serif;font-weight:400;font-size:19px;line-height:28px;margin-top:22px}
.testi p{font-size:14px;line-height:26px;color:var(--muted);margin-top:10px}
.testi .who{font-size:14px;font-weight:700;margin-top:18px}
.testi .role{font-size:11px;color:var(--muted);margin-top:4px}
.dots{left:550px;top:4200px;display:flex;gap:8px}
.dots i{width:9px;height:9px;border-radius:50%;background:#f0dfc7;display:block}
.dots i.on{background:var(--gold)}

/* footer */
.site-footer{position:absolute;top:4295px;left:0;width:1200px;height:399px;background:var(--navy);color:var(--white)}
.site-footer h5{font-size:20px;font-weight:600;position:absolute;top:98px}
.site-footer ul{list-style:none;position:absolute;top:141px;font-size:14px;line-height:29px}
.contact-row{position:absolute;left:835px;display:flex;gap:14px;font-size:14px;line-height:21px;width:300px}
</style>
</head>
<body>

<header class="site-header">
  <div class="brand"><div class="mark"></div><div class="name">Brightwell</div><div class="sub">LAW FIRM</div></div>
  <nav class="main-nav"><span>Home</span><span>About Us</span><span>Practice Areas</span><span>Our Strategy</span><span>Testimonials</span><span>Contact Us</span></nav>
  <span class="signin">Sign In</span>
  <span class="btn" style="left:1018px;top:18px;width:111px;height:40px">Sign Up</span>
</header>

<section class="hero">
  <div class="ph" role="img" aria-label="Two lawyers in suits standing before classical columns" style="left:547px;top:0;width:653px;height:584px;background:linear-gradient(90deg,#0f1330 0%,#3a3a48 35%,#8a7a62 70%,#c8b08a 100%)"></div>
  <h1 class="serif">Injured in an Accident? Get the Compensation You Deserve!</h1>
  <p>No Fees Unless We Win. Experienced Personal Injury Lawyers Fighting for You!</p>
  <span class="btn" style="left:70px;top:400px;width:180px;height:42px">Free Consultation</span>
</section>

<section class="about">
  <div class="abs about-deco"></div>
  <div class="ph" role="img" aria-label="Team of lawyers talking outside an office building" style="left:70px;top:793px;width:543px;height:376px;background:linear-gradient(160deg,#7f8a86,#3e4a50 55%,#9aa2a4)"></div>
  <h2 class="abs serif section-title" style="left:667px;top:796px">Brightwell Law Firm</h2>
  <p class="abs body-copy" style="left:667px;top:854px;width:445px">Justice. Recovery. A Better Future Starts Here At The Brightwell Law Firm, we understand that suffering a personal injury can be life-altering—physically, emotionally, and financially. You may be unsure whether pursuing legal action is the right step. But in Florida, holding negligent parties accountable isn't just your right—it's often necessary to rebuild your life. We take a concierge-style approach to personal injury law, offering personalized attention, strategic advocacy, and relentless dedication to securing the maximum compensation you deserve.</p>
  <span class="btn" style="left:667px;top:1116px;width:133px;height:40px">Learn More</span>
</section>

<section class="band" style="top:1298px;height:593px">
  <h2 class="abs serif section-title center" style="top:50px;font-size:42px">Our Strategy</h2>
  <p class="abs center" style="top:108px;font-size:16px;line-height:28px;color:#55555c">default model text, and a search for 'lorem ipsum' will uncover many web<br>sites still in their infancy. Various versions have evolved years,</p>
  <div class="abs strat-card" style="left:100px;top:203px;width:316px">
    <div role="img" aria-label="Three lawyers walking across a plaza" style="height:191px;background:linear-gradient(135deg,#b9a58a,#6e7378 60%,#c9ccd0)"></div>
    <div class="t serif">Taking On Corporate Giants</div>
    <div class="d">looked up one of the more obscure has words consectetur, from a lorem is Ipsum passage do and going...</div>
    <div class="l">Learn More →</div>
  </div>
  <div class="abs strat-card" style="left:441px;top:203px;width:316px">
    <div role="img" aria-label="Lawyers meeting a client at a café table" style="height:191px;background:linear-gradient(135deg,#8c8f96,#3c4250 60%,#bfc3c9)"></div>
    <div class="t serif">Concierge-Style Legal Care</div>
    <div class="d">looked up one of the more obscure has words consectetur, from a lorem is Ipsum passage do and going...</div>
    <div class="l">Learn More →</div>
  </div>
  <div class="abs strat-card" style="left:782px;top:203px;width:318px">
    <div role="img" aria-label="Lawyer and client discussing documents at a desk" style="height:191px;background:linear-gradient(135deg,#e4e4e6,#7a7f88 55%,#c23a3a)"></div>
    <div class="t serif">No Win, No Fee Guarantee</div>
    <div class="d">looked up one of the more obscure has words consectetur, from a lorem is Ipsum passage do and going...</div>
    <div class="l">Learn More →</div>
  </div>
</section>

<section class="why">
  <div class="abs" style="left:717px;top:1973px;width:483px;height:467px;background:linear-gradient(225deg,#f1f1f3,#fbfbfc)"></div>
  <h2 class="abs serif section-title" style="left:70px;top:2040px;width:470px;line-height:56px">Why Choose The Brightwell Law Firm?</h2>
  <p class="abs" style="left:70px;top:2162px;font-size:15px;color:var(--ink)">Unmatched Experience Proven Results Relentless Advocacy.</p>
  <p class="abs body-copy" style="left:70px;top:2195px;width:450px;line-height:28.5px">A client fell eight feet at a major sporting venue and suffered catastrophic injuries. We recovered compensation that covered all medical bills, paid off their home, and funded their children's college education A client suffered a severe infection from a minor slip-and-fall injury in a Miami condo building...</p>
  <div class="ph" role="img" aria-label="Hands signing a contract on a wooden desk" style="left:587px;top:2021px;width:542px;height:374px;background:linear-gradient(135deg,#1d2230,#3b3a3c 50%,#8a6d4e 75%,#d8d8da)"></div>
</section>

<section>
  <div class="feature dark" style="left:75px;width:332px">
    <div class="head">
      <svg width="54" height="54" viewBox="0 0 54 54" fill="none" stroke="#fff" stroke-width="1.6"><circle cx="27" cy="22" r="15"/><circle cx="27" cy="22" r="10"/><text x="27" y="26" font-size="10" fill="#fff" stroke="none" text-anchor="middle" font-family="Open Sans">25</text><path d="M8 44h38M12 44v-6h30v6"/></svg>
      <span>25+ Years of Legal Mastery</span>
    </div>
    <p>We have successfully handled thousands of cases, fighting both for and against insurance companies. This unique dual experience gives us an insider advantage in every case we take on.</p>
  </div>
  <div class="feature" style="left:432px;width:334px">
    <div class="head">
      <svg width="54" height="54" viewBox="0 0 54 54" fill="none" stroke="#333" stroke-width="1.6"><path d="M27 6v34M14 40h26M10 18h34"/><path d="M10 18l-6 12h12zM44 18l-6 12h12z"/><circle cx="27" cy="8" r="3"/></svg>
      <span>Extensive Knowledge of Insurance Tactics</span>
    </div>
    <p>Having worked for insurance companies, we know their strategies, loopholes, and how to dismantle their defenses to maximize your settlement.</p>
  </div>
  <div class="feature" style="left:792px;width:333px">
    <div class="head">
      <svg width="54" height="54" viewBox="0 0 54 54" fill="none" stroke="#333" stroke-width="1.6"><circle cx="15" cy="14" r="7"/><circle cx="39" cy="14" r="7"/><circle cx="10" cy="38" r="7"/><circle cx="27" cy="38" r="7"/><circle cx="44" cy="38" r="7"/><path d="M27 8v14M23 18l4 4 4-4"/></svg>
      <span>Millions Recovered for Clients</span>
    </div>
    <p>Our track record highlights life-changing results, securing justice and maximum compensation for our clients.</p>
  </div>
</section>

<section class="band" style="top:2781px;height:797px">
  <h2 class="abs serif section-title center" style="top:60px;font-size:40px">Our Practice Area</h2>
  <p class="abs center" style="top:124px;font-size:16px;line-height:29px;color:#55555c">looked up one of the more obscure Latin words, consectetur, from a Lorem Ipsum<br>passage, and going through the cites of the word in classical...</p>
  <div class="divider" style="left:421px;top:225px;height:240px"></div>
  <div class="divider" style="left:777px;top:225px;height:240px"></div>
  <div class="divider" style="left:421px;top:498px;height:245px"></div>
  <div class="divider" style="left:777px;top:498px;height:245px"></div>

  <div class="practice" style="left:122px;top:225px">
    <svg width="80" height="75" viewBox="0 0 80 75" fill="none" stroke="#d4a86a" stroke-width="2"><path d="M6 44h24l6-10h14l6 10h14v10H6z"/><circle cx="20" cy="56" r="5"/><circle cx="62" cy="56" r="5"/><path d="M40 14l4 10 10-6-4 10 10 2-10 4"/></svg>
    <h3>Car Accidents</h3>
    <p>We Fight For Victims Of Rear-End Crashes, Multi-Vehicle Collisions, Pedestrian And Cyclist Accidents, And More.</p>
  </div>
  <div class="practice" style="left:476px;top:225px">
    <svg width="80" height="85" viewBox="0 0 80 85" fill="none" stroke="#d4a86a" stroke-width="2"><path d="M50 4l-14 76M66 4L52 80M48 20h14M45 36h14M42 52h14M39 68h14"/><circle cx="16" cy="30" r="6"/><path d="M16 36v20l-8 16M16 46l14-6"/></svg>
    <h3>Slip And Fall</h3>
    <p>Premises Liability: If You Were Injured Due To Unsafe Conditions At A Business, Hotel, Condo, Or Public Space, We Hold Negligent</p>
  </div>
  <div class="practice" style="left:832px;top:225px">
    <svg width="80" height="78" viewBox="0 0 80 78" fill="none" stroke="#d4a86a" stroke-width="2"><rect x="6" y="4" width="50" height="66"/><path d="M16 46h30M16 54h30M16 62h20M31 12v22M24 19h14"/><circle cx="62" cy="52" r="9"/><path d="M58 60l-3 12 7-4 7 4-3-12"/></svg>
    <h3>Wrongful Death</h3>
    <p>We Provide Compassionate Yet Fierce Representation For Families Who Have Lost A Loved One Due To Negligence.</p>
  </div>

  <div class="practice" style="left:122px;top:498px">
    <svg width="80" height="82" viewBox="0 0 80 82" fill="none" stroke="#d4a86a" stroke-width="2"><circle cx="40" cy="18" r="12"/><circle cx="40" cy="18" r="5"/><path d="M6 40h68v36H6zM6 40l8-10h52l8 10M32 40v14h16V40"/></svg>
    <h3>Product Liability</h3>
    <p>If A Dangerous Product Caused Your Injury, We Pursue Manufacturers, Distributors, And Retailers For Maximum Compensation.</p>
  </div>
  <div class="practice" style="left:476px;top:498px">
    <svg width="90" height="82" viewBox="0 0 90 82" fill="none" stroke="#d4a86a" stroke-width="2"><circle cx="24" cy="16" r="11"/><path d="M6 78V42q0-12 18-12t18 12v36M24 30v48"/><rect x="48" y="44" width="36" height="28"/><path d="M60 44v-6h12v6M48 56h36"/></svg>
    <h3>Workplace Injuries</h3>
    <p>If A Third Party's Negligence Contributed To Your Workplace Injury, We Help You Seek Compensation Beyond Workers</p>
  </div>
  <div class="practice" style="left:832px;top:498px">
    <svg width="90" height="82" viewBox="0 0 90 82" fill="none" stroke="#d4a86a" stroke-width="2"><circle cx="56" cy="12" r="7"/><path d="M54 20l-12 20 14 10-6 24M42 40l-12 16M54 26l16 10M42 40l-14-8"/><path d="M6 60q6-10 18-8l8 6-6 6H12l-4 12M24 64l4 12"/></svg>
    <h3>Dog Bites Attacks</h3>
    <p>Florida's Strict Liability Laws Mean Pet Owners Are Responsible For Injuries Caused By Their Animals.</p>
  </div>
</section>

<section>
  <h2 class="abs serif section-title center" style="top:3650px;font-size:40px">Our Testimonials</h2>
  <p class="abs center" style="top:3712px;font-size:16px;line-height:29px;color:#55555c">looked up one of the more obscure Latin words, consectetur, from a Lorem Ipsum<br>passage, and going through the cites of the word in classical...</p>
  <div class="testi" style="left:71px"><div class="q">“</div><h4>Fact That A Reader Will Be Distracted By The</h4><p>Content of a page when looking at its layout. The point of using Lorem Ipsum is that it has a more-or-less normal distribution of letters, as opposed to using 'Content here,</p><div class="who">Nora P</div><div class="role">more-or-less normal distribution</div></div>
  <div class="testi" style="left:434px"><div class="q">“</div><h4>Fact That A Reader Will Be Distracted By The</h4><p>Content of a page when looking at its layout. The point of using Lorem Ipsum is that it has a more-or-less normal distribution of letters, as opposed to using 'Content here,</p><div class="who">Marcus L</div><div class="role">more-or-less normal distribution</div></div>
  <div class="testi" style="left:797px"><div class="q">“</div><h4>Fact That A Reader Will Be Distracted By The</h4><p>Content of a page when looking at its layout. The point of using Lorem Ipsum is that it has a more-or-less normal distribution of letters, as opposed to using 'Content here,</p><div class="who">Clara V</div><div class="role">more-or-less normal distribution</div></div>
  <div class="abs dots"><i></i><i></i><i class="on"></i><i></i><i></i><i></i></div>
</section>

<footer class="site-footer">
  <div class="brand" style="left:72px;top:100px;width:130px;color:var(--white)"><div class="mark" style="width:26px;height:26px"></div><div class="name" style="font-size:28px;line-height:30px">Brightwell</div><div class="sub">LAW FIRM</div></div>
  <p class="abs" style="left:71px;top:180px;width:320px;font-size:14px;line-height:26px">Content of a page when looking at its layout The point of using Lorem Ipsum less normal distribution...</p>
  <div class="abs" style="left:71px;top:276px;display:flex;gap:12px"><i style="width:16px;height:16px;border-radius:50%;background:var(--white);display:block"></i><i style="width:16px;height:16px;border-radius:50%;background:var(--white);display:block"></i><i style="width:16px;height:16px;border-radius:50%;background:var(--white);display:block"></i></div>

  <h5 style="left:485px">Quick Links</h5>
  <ul style="left:485px"><li>Home</li><li>About Us</li><li>Our Teams</li><li>Practice Area</li><li>Blogs</li></ul>
  <h5 style="left:653px">Support</h5>
  <ul style="left:653px"><li>Contact Us</li><li>Helps</li><li>Privacy Policy</li><li>Terms &amp; Condition</li></ul>
  <h5 style="left:835px">Contact Us</h5>
  <div class="contact-row" style="top:140px"><svg width="16" height="20" viewBox="0 0 16 20"><path d="M8 0a7 7 0 0 0-7 7c0 5 7 13 7 13s7-8 7-13a7 7 0 0 0-7-7z" fill="#fff"/><circle cx="8" cy="7" r="2.5" fill="#0f1330"/></svg><span>ontent of a page when looking at its layout.</span></div>
  <div class="contact-row" style="top:194px"><svg width="18" height="14" viewBox="0 0 18 14"><rect width="18" height="14" rx="1" fill="#fff"/><path d="M1 1l8 7 8-7" stroke="#0f1330" stroke-width="1.5" fill="none"/></svg><span>hello@brightwelllaw.example</span></div>
  <div class="contact-row" style="top:230px"><svg width="17" height="17" viewBox="0 0 24 24"><path fill="#fff" d="M6.6 10.8a15 15 0 0 0 6.6 6.6l2.2-2.2a1 1 0 0 1 1-.25 11.4 11.4 0 0 0 3.6.57 1 1 0 0 1 1 1V20a1 1 0 0 1-1 1A17 17 0 0 1 3 4a1 1 0 0 1 1-1h3.5a1 1 0 0 1 1 1c0 1.25.2 2.45.57 3.57a1 1 0 0 1-.25 1z"/></svg><span>(305) 555-0148</span></div>

  <div class="abs" style="left:71px;top:328px;width:1058px;height:1px;background:rgba(255,255,255,.35)"></div>
  <p class="abs center" style="top:352px;font-size:12px">© 2025 Personal-Injury-Law-Firm. All rights reserved.</p>
</footer>

</body>
</html>
```